Business Card Design

Looking for business card designs for a new business. there will be two cards of the same design (both lots of information below in contact info). We would like the logo diagonally across the card with the information split above and below the logo similar to sketch. happy to look at similar alternatives
Please use same colours as in logo design

Industry/Entity Type

Business

Contact Information for Business Card

Gareth Mullins
mob - 0498 172 309
ph - 02 4839 2100
fax - 02 4839 2400
email - gaz@ridgelinetrusses.com.au
14 Calloway Road, Parrinda NSW 2340

Desmond Alcott
mob - 0426 918 753
ph - 02 4839 2100
fax - 02 4839 2400
email - desmond@ridgelinetrusses.com.au

```html
<!DOCTYPE html>
<html lang="en">
<head>
<meta charset="utf-8">
<title>Ridgeline Frames &amp; Trusses – Business Card</title>
<link rel="stylesheet" href="https://fonts.googleapis.com/css2?family=Open+Sans:wght@400;600;700&display=swap">
<style>
  :root {
    --backdrop-light: #5a5a5b;
    --backdrop-dark: #2e2e2f;
    --card-white: #ffffff;
    --teal: #0c7f7d;
    --teal-dark: #0a6665;
    --band-grey: #cfd0d2;
    --ink: #111111;
    --text-light: #ffffff;
  }
  html, body {
    margin: 0;
    padding: 0;
    width: 1200px;
    height: 999px;
    overflow: hidden;
  }
  body {
    background: radial-gradient(ellipse at 50% 45%, var(--backdrop-light) 0%, var(--backdrop-dark) 80%);
    font-family: "Open Sans", Arial, sans-serif;
    position: relative;
  }
  .card {
    position: absolute;
    left: 75px;
    top: 199px;
    width: 1050px;
    height: 600px;
    background: var(--card-white);
  }
  .card-shapes {
    position: absolute;
    left: 0;
    top: 0;
  }
  .brand {
    position: absolute;
    left: 35px;
    top: 62px;
    display: flex;
    align-items: flex-start;
    gap: 14px;
    color: var(--ink);
    font-weight: 600;
  }
  .brand-mark {
    width: 26px;
    height: 26px;
    background: var(--teal);
    margin-top: 16px;
  }
  .brand-name {
    margin: 0;
    line-height: 1;
  }
  .brand-name .primary {
    display: block;
    font-size: 74px;
    letter-spacing: -1px;
  }
  .brand-name .secondary {
    display: block;
    font-size: 38px;
    margin-top: 4px;
    margin-left: 4px;
  }
  .person-name {
    position: absolute;
    left: 61px;
    top: 357px;
    margin: 0;
    font-size: 33px;
    font-weight: 700;
    color: var(--text-light);
    line-height: 1;
  }
  .contact-list {
    position: absolute;
    left: 38px;
    top: 420px;
    margin: 0;
    padding: 0;
    list-style: none;
    color: var(--text-light);
    font-size: 24px;
  }
  .contact-list li {
    display: flex;
    align-items: center;
    height: 35px;
  }
  .contact-list svg {
    width: 24px;
    height: 24px;
    flex: none;
  }
  .contact-list .divider {
    display: inline-block;
    width: 2px;
    height: 24px;
    background: var(--text-light);
    margin: 0 14px 0 14px;
  }
  .address {
    position: absolute;
    left: 645px;
    top: 457px;
    margin: 0;
    font-style: normal;
    font-size: 24px;
    line-height: 35px;
    color: var(--text-light);
  }
</style>
</head>
<body>
  <section class="card" aria-label="Business card for Gareth Mullins">
    <svg class="card-shapes" width="1050" height="600" viewBox="0 0 1050 600" aria-hidden="true">
      <!-- grey bands -->
      <polygon points="0,398 738,398 677,586 0,586" fill="var(--band-grey)"/>
      <polygon points="755,412 1050,412 1050,586 693,586" fill="var(--band-grey)"/>
      <!-- name tab flanks -->
      <polygon points="25,398 40,352 40,398" fill="var(--ink)"/>
      <polygon points="385,398 370,352 370,398" fill="var(--ink)"/>
      <!-- name tab -->
      <rect x="40" y="352" width="330" height="60" fill="var(--teal-dark)"/>
      <!-- teal contact panel -->
      <polygon points="0,412 622,412 570,568 0,568" fill="var(--teal)"/>
      <!-- teal address panel -->
      <polygon points="630,444 1050,444 1050,546 596,546" fill="var(--teal)"/>
    </svg>

    <div class="brand">
      <span class="brand-mark"></span>
      <h1 class="brand-name">
        <span class="primary">Ridgeline</span>
        <span class="secondary">frames &amp; trusses</span>
      </h1>
    </div>

    <h2 class="person-name">Gareth Mullins</h2>

    <ul class="contact-list">
      <li>
        <svg viewBox="0 0 24 24" aria-label="Mobile">
          <rect x="2" y="1" width="20" height="22" rx="4" fill="#fff"/>
          <rect x="6" y="5" width="12" height="14" fill="var(--teal)"/>
          <line x1="8" y1="7" x2="16" y2="17" stroke="#fff" stroke-width="1.6"/>
        </svg>
        <span class="divider"></span>0498 172 309
      </li>
      <li>
        <svg viewBox="0 0 24 24" aria-label="Phone">
          <rect x="2" y="1" width="20" height="22" rx="4" fill="#fff"/>
          <path d="M9 6 C7 8 8 14 13 18 L15.5 16 L13.5 14 L12 15 C10.5 13.5 10 12 10 10.5 L11.5 9.5 Z" fill="var(--teal)"/>
        </svg>
        <span class="divider"></span>02 4839 2100
      </li>
      <li>
        <svg viewBox="0 0 24 24" aria-label="Fax">
          <rect x="6" y="1" width="12" height="8" fill="#fff"/>
          <rect x="2" y="10" width="20" height="8" rx="1" fill="#fff"/>
          <rect x="5" y="19" width="14" height="4" fill="#fff"/>
        </svg>
        <span class="divider"></span>02 4839 2400
      </li>
      <li>
        <svg viewBox="0 0 24 24" aria-label="Email">
          <path d="M2 10 L12 3 L22 10 L22 21 L2 21 Z" fill="#fff"/>
          <path d="M2 10 L12 16 L22 10" fill="none" stroke="var(--teal)" stroke-width="1.6"/>
        </svg>
        <span class="divider"></span>gaz@ridgelinetrusses.com.au
      </li>
    </ul>

    <address class="address">
      14 Calloway Road,<br>
      Parrinda NSW 2340 Desmond
    </address>
  </section>
</body>
</html>
```